Happy Birthday Postcard for law firm for existing clients

Need a postcard that will go out to our current clients on their birthdays. Prefer to have our logo incorporated as part of the design so it reminds them about our business. The back needs to say "Happy Birthday from the team at Brantley Law Firm."

We are a law firm that services local clients. Needs to be mailed so the backside right half needs to be left blank except the return address (in NEEDS below) so it can be mailed with a mailing label.

Target Market(s)

existing customers, varying age range and demographic profile

Industry/Entity Type

Legal

Font styles to use
Sans Serif
Script

Colors

Designer to choose colors to be used in the design.

Requirements
Must have
• Our logo preferrably on the front (can be modified or added to so it fits a birthday message. And needs to be mailed so the back right side needs to be left open for address labels. The firms return address is
• Brantley Law Firm
• 7150 W Copperfield Ave
• Springfield, MO 65817
• Needs to have the text included in the project description on the back, or some close iteration of it if space is limited.
Nice to have
• Some illustration or graphic on the front with the logo that shows it is a birthday postcard

```html
<!DOCTYPE html>
<html lang="en">
<head>
<meta charset="utf-8">
<title>Brantley Law Firm – Birthday Postcard</title>
<link href="https://fonts.googleapis.com/css2?family=Great+Vibes&family=Poiret+One&family=Montserrat:wght@400&family=Crimson+Text&family=Open+Sans:ital,wght@0,400;1,600&display=swap" rel="stylesheet">
<style>
  :root {
    --backdrop: #8b5e3c;
    --card-dark: #0b0b0b;
    --card-light: #ffffff;
    --gold: #f0a020;
    --gold-light: #f7d23a;
    --lavender: #8d92bd;
    --slate: #68686b;
    --zone-grey: #e6e7e8;
    --ink: #111111;
    --muted: #6b6b6b;
  }
  * { margin: 0; padding: 0; box-sizing: border-box; }
  html, body { width: 810px; height: 1200px; overflow: hidden; background: var(--backdrop); }
  .canvas { position: relative; width: 810px; height: 1200px; }

  .card {
    position: absolute; left: 52px; width: 696px;
    box-shadow: 6px 8px 10px rgba(0,0,0,0.35);
    overflow: hidden;
  }

  /* Front */
  .card-front { top: 48px; height: 538px; background: var(--card-dark); }
  .festive-illustration {
    position: absolute; inset: 0;
    background: radial-gradient(ellipse 340px 230px at 300px 150px, rgba(240,170,40,0.22), rgba(240,170,40,0) 100%);
  }
  .front-backdrop { position: absolute; inset: 0; }
  .front-greeting {
    position: absolute; left: 34px; top: 384px;
    font-family: "Great Vibes", cursive; font-size: 42px; font-weight: 400;
    color: var(--gold); line-height: 1; white-space: nowrap;
  }
  .front-signoff {
    position: absolute; left: 34px; top: 436px;
    font-family: "Poiret One", sans-serif; font-size: 17px; color: var(--gold); white-space: nowrap;
  }
  .front-mark {
    position: absolute; left: 470px; top: 392px; width: 48px; height: 48px;
    background: var(--lavender);
  }
  .front-name {
    position: absolute; left: 326px; top: 470px; width: 360px; text-align: center;
    font-family: "Montserrat", sans-serif; font-weight: 400; font-size: 38px;
    letter-spacing: 1px; color: var(--slate); line-height: 1; white-space: nowrap;
  }

  /* Back */
  .card-back { top: 614px; height: 540px; background: var(--card-light); }
  .zone {
    position: absolute; background: var(--zone-grey);
    font-family: Arial, Helvetica, sans-serif; font-size: 18px; color: var(--ink);
    text-align: center; line-height: 1.4;
  }
  .zone-postage { left: 523px; top: 18px; width: 155px; height: 154px; padding-top: 48px; }
  .zone-address { left: 337px; top: 172px; width: 341px; height: 273px; padding-top: 48px; }
  .zone-barcode { left: 87px; top: 444px; width: 591px; height: 78px; padding-top: 30px; }

  .back-column { position: absolute; left: 16px; top: 0; width: 320px; height: 444px; }
  .back-column > * { position: absolute; left: 0; width: 320px; text-align: center; white-space: nowrap; }
  .back-greeting {
    top: 22px; font-family: "Great Vibes", cursive; font-weight: 400;
    font-size: 52px; color: var(--gold); line-height: 1;
  }
  .back-from, .back-firm {
    font-family: "Crimson Text", serif; color: var(--lavender); font-size: 25px; line-height: 1;
  }
  .back-from { top: 94px; }
  .back-firm { top: 126px; }
  .back-mark { top: 184px; left: 136px !important; width: 48px !important; height: 48px; background: var(--lavender); }
  .back-name {
    top: 264px; font-family: "Montserrat", sans-serif; font-weight: 400;
    font-size: 32px; color: var(--slate); line-height: 1;
  }
  .back-rule {
    top: 314px; left: 24px !important; width: 272px !important; height: 4px; border-radius: 2px;
    background: linear-gradient(90deg, var(--gold), var(--gold-light) 55%, var(--gold));
  }
  .return-label {
    top: 338px; font-family: "Open Sans", sans-serif; font-style: italic;
    font-weight: 600; font-size: 15px; color: var(--muted); line-height: 1.2;
  }
  .return-address {
    top: 364px; font-family: "Open Sans", sans-serif; font-style: normal;
    font-size: 16px; color: var(--ink); line-height: 1.3;
  }
</style>
</head>
<body>
<main class="canvas">

  <section class="card card-front">
    <div class="festive-illustration" role="img" aria-label="Golden bead garlands, hanging star ornaments and sparkles"></div>
    <svg class="front-backdrop" width="696" height="538" viewBox="0 0 696 538">
      <defs>
        <linearGradient id="fold-edge" x1="0" y1="1" x2="1" y2="0">
          <stop offset="0" stop-color="#8d92bd" stop-opacity="0"/>
          <stop offset="1" stop-color="#8d92bd" stop-opacity="0.9"/>
        </linearGradient>
      </defs>
      <polygon points="206,538 696,190 696,202 216,538" fill="url(#fold-edge)"/>
      <polygon points="216,538 696,196 696,538" fill="#ffffff"/>
    </svg>
    <h1 class="front-greeting">Happy Birthday</h1>
    <p class="front-signoff">from the team at Brantley Law Firm</p>
    <div class="front-mark"></div>
    <p class="front-name">BRANTLEY LAW</p>
  </section>

  <section class="card card-back">
    <div class="back-column">
      <h2 class="back-greeting">Happy Birthday</h2>
      <p class="back-from">from the team at</p>
      <p class="back-firm">BRANTLEY LAW FIRM</p>
      <div class="back-mark"></div>
      <p class="back-name">BRANTLEY LAW</p>
      <div class="back-rule"></div>
      <p class="return-label">Return address</p>
      <address class="return-address">Brantley Law Firm<br>7150 W Copperfield Ave<br>Springfield, MO 65817</address>
    </div>
    <div class="zone zone-postage">Postage<br>Area</div>
    <div class="zone zone-address">Address Area</div>
    <div class="zone zone-barcode">Barcode Area</div>
  </section>

</main>
</body>
</html>
```